Brackwell Powerpoint Template

We need a .pptx template for company presentations.

It is comprised of only two pages:

1) cover page
2) inside pages

Both pages should be based on our logo, attached on the brief.

The cover page must have space for title and subtitle.
Updates

Update on the brief:

We are looking for a cover page that is not too "busy" or complicated. Dark background is preferred, especially if it plays with the logo colors (maybe playing with a negative version of it).

The inside page has also to be simple: no arrows or anything similar. Keep in mind that those presentations will be printed in paper.

The inside page should have the logo either on the top right corner or on the bottom right corner.

A good way to separate the title (or to create space for it) would be to play with the horizon line from the logo maybe a thinner version of it, since it will have to be much longer).

The inside page must have a white background and a place for the page number.

Target Market(s)

High end investors

Industry/Entity Type

It Company

```html
<!DOCTYPE html>
<html lang="en">
<head>
<meta charset="utf-8">
<title>Brackwell – Color Palette</title>
<link rel="stylesheet" href="https://fonts.googleapis.com/css2?family=Mulish:wght@400;700;800&display=swap">
<style>
  :root {
    --frame: #efece2;
    --slide-light: #f1f1f1;
    --slide-dark: #dcdcdc;
    --brand-blue: #0077a8;
    --rule-dark: #58585a;
    --rule-thin: #8a8a8a;
    --text-gray: #5a5a5a;
    --blue-main: #0077aa;
    --blue-deep: #02506f;
    --blue-mid: #235f80;
    --blue-light: #37a9d6;
    --orange-main: #ff8400;
    --orange-deep: #a85400;
    --orange-mid: #c07830;
    --orange-light: #ffa040;
    --gray-main: #58585a;
    --gray-deep: #7f7f7f;
    --gray-mid: #a5a5a5;
    --gray-light: #bfbfbf;
    --divider: #ffffff;
  }
  * { box-sizing: border-box; margin: 0; padding: 0; }
  html, body { width: 1200px; height: 900px; overflow: hidden; background: var(--frame); }
  .slide {
    position: absolute; left: 22px; top: 25px; width: 1156px; height: 850px;
    background: linear-gradient(225deg, var(--slide-light) 0%, var(--slide-dark) 100%);
    font-family: "Mulish", sans-serif;
  }
  .slide-title {
    position: absolute; left: 40px; top: 50px;
    font-size: 42px; font-weight: 800; color: var(--brand-blue); letter-spacing: -0.5px;
  }
  .title-rule-thin {
    position: absolute; left: 40px; top: 125px; width: 1091px; height: 1px; background: var(--rule-thin);
  }
  .title-rule-bar {
    position: absolute; left: 38px; top: 122px; width: 205px; height: 8px; background: var(--rule-dark);
  }
  .palette { position: absolute; left: 0; top: 0; }
  .company-name {
    position: absolute; left: 40px; top: 783px;
    font-size: 30px; font-weight: 400; color: var(--text-gray); letter-spacing: 1px;
  }
  .page-number {
    position: absolute; left: 942px; top: 798px; font-size: 16px; color: var(--text-gray);
  }
  .page-marker {
    position: absolute; left: 988px; top: 800px; width: 145px; height: 15px;
    background: repeating-linear-gradient(-45deg, var(--rule-dark) 0 2px, #c9c9c9 2px 4px);
  }
</style>
</head>
<body>
<div class="slide">
  <h1 class="slide-title">Color Palette</h1>
  <div class="title-rule-thin"></div>
  <div class="title-rule-bar"></div>

  <svg class="palette" width="1156" height="850" viewBox="22 25 1156 850" aria-label="Colour swatches">
    <defs>
      <clipPath id="clip-blue"><circle cx="355" cy="425" r="108"/></clipPath>
      <clipPath id="clip-orange"><circle cx="637" cy="428" r="108"/></clipPath>
      <clipPath id="clip-gray"><circle cx="896" cy="425" r="108"/></clipPath>
    </defs>

    <g class="swatch-blue" clip-path="url(#clip-blue)">
      <rect x="240" y="310" width="230" height="88" fill="var(--blue-main)"/>
      <rect x="240" y="398" width="82" height="140" fill="var(--blue-deep)"/>
      <rect x="322" y="398" width="73" height="140" fill="var(--blue-mid)"/>
      <rect x="395" y="398" width="75" height="140" fill="var(--blue-light)"/>
      <path d="M240 398H470M322 398V540M395 398V540" stroke="var(--divider)" stroke-width="2"/>
    </g>

    <g class="swatch-orange" clip-path="url(#clip-orange)">
      <rect x="522" y="313" width="230" height="89" fill="var(--orange-main)"/>
      <rect x="522" y="402" width="82" height="140" fill="var(--orange-deep)"/>
      <rect x="604" y="402" width="73" height="140" fill="var(--orange-mid)"/>
      <rect x="677" y="402" width="75" height="140" fill="var(--orange-light)"/>
      <path d="M522 402H752M604 402V542M677 402V542" stroke="var(--divider)" stroke-width="2"/>
    </g>

    <g class="swatch-gray" clip-path="url(#clip-gray)">
      <rect x="781" y="310" width="230" height="92" fill="var(--gray-main)"/>
      <rect x="781" y="402" width="82" height="140" fill="var(--gray-deep)"/>
      <rect x="863" y="402" width="72" height="140" fill="var(--gray-mid)"/>
      <rect x="935" y="402" width="76" height="140" fill="var(--gray-light)"/>
      <path d="M781 402H1011M863 402V540M935 402V540" stroke="var(--divider)" stroke-width="2"/>
    </g>
  </svg>

  <div class="company-name">Brackwell Capital Partners</div>
  <div class="page-number">4</div>
  <div class="page-marker"></div>
</div>
</body>
</html>
```